dentist office tri-fold for root canal specialist

design a tri fold brochure to give to patients talking about the office and the services
Talk about doctors and their bios
services: root canal , retreatments, endodontic surgery, trauma, cracked teeth
Technology: CBCT, microscopes, lasers, clear pulse advanced
I will provide all the technical info. willing to hire a writer if needed. Attached a picture of our logo as a reference of our colors. Can attach older versions of brochure if requested. Looking for a very professional tri fold that will be used to market the practice to patients and other doctors.
Rough idea: TRIFOLD
Front Cover:
Welcome to The Halvern Team
Thank you for allowing us to care for your endodontic needs. We look forward to serving you.
We at The Halvern Team have dedicated our professional lives to improving the comfort and dental health of those in our care.
Inner Right:
Pics of Docs
Welcome – On behalf of our staff, we welcome you to our office.
We are pleased that you have selected our team of professionals to care for your endodontic needs. We want you to know that we are committed to providing you, our patient with the highest quality endodontic care in the most gentle, efficient, and caring manner possible. We pride ourselves on offering our expertise along with the best patient care with the most up to date technologies to better ensure your oral health.
For your convenience, please visit us online at www.thehalvernteam.com for directions to our offices, pre and post-operative instructions, general information on our Endodontists and much more. We are here for you and our doctors are on call 24 hours a day, 7 days a week.
We are looking forward providing you a most relaxed and pleasant vist possible. Thank you again for choosing The Halvern Team.
Inner Middle:
What is a Root Canal?
A root canal (endodontic treatment) is one of the most common dental procedures performed, with more than 14 million performed every year. This simple treatment can save your natural teeth and prevent the need of dental implants or bridges.
At the center of your tooth is pulp. The pulp is a collection of blood vessels, nerves and lymphatics, which help to form the tooth during the stages of tooth development.
I’ve already had a root canal, why do I need another procedure?
Retreatment - A second chance to save your tooth
With proper care, most teeth which have had endodontic (root canal) treatment can last as long as other natural teeth.
However, in a few cases, a tooth that has received endodontic treatment fails to heal completely. And occasionally, a tooth becomes painful or diseased months or even years after previously successful endodontic treatment.
If your tooth has failed to heal or has developed new problems, you have a second chance. Another endodontic procedure, called retreatment, may be able to save your tooth.
Retreated teeth can function well for years, even for a lifetime. It's always best to save the tooth if your endodontist believes retreatment is the best option for you.
Advances in technology are constantly changing the way root canal treatment is performed, so your endodontist may even be able to use a new technique that was not available when you had your first procedure.
Of course, there are no guarantees with any dental or medical procedure. Your endodontist will discuss your options and the chances of success before beginning retreatment.
What is an Apicoectomy?
In this procedure, the endodontist opens the gum tissue near the tooth to see the underlying bone and to remove any inflamed or infected tissue. The very end of the root is also removed or resected.
Inner Right:
Patient Care: Needing a root canal is often a surprise and sometimes an emergency. We at The Halvern Team make certain that every patient receives prompt emergency care at any time.
We understand how uneasy some patients may feel about dental visits and how we can make a difference in providing a relaxing, positive experience. Our doctors are trained in different levels of sedation dentistry from Nitrous Oxide to Conscious Sedation.
Our entire team is dedicated to providing you with excellent, personalized care and service to make your visit as comfortable and pleasant as possible. You will enjoy our relaxing treatment rooms, complete with plumacore coverings, televisions and Tunelets for your use during treatment and blankets to keep you warm if you’re cold.
Technical Equipment: The Halvern Team prides itself in utilizing the most advanced techniques and state-of-the-art equipment including digital radiography, fiber optic illumination, ultrasonic equipment, and operating microscopes, which help the doctor see microscopic details inside a tooth during micro-surgical and non-surgical procedures.
Expertise: The Halvern Team is staffed by doctors who are responsive to your concerns and alert to your experience during treatment. All of our doctors are endodontists, which means they are specialists who have completed 2-3 years of advanced training in addition to dental school. We are all specialist members of the Continental Society of Pulp Specialists (CSPS). All our endodontists continue their education and training through professional associations, seminars, study groups, and teaching both at Pellmoor and Dorrin Universities.

```html
<!DOCTYPE html>
<html lang="en">
<head>
<meta charset="utf-8">
<title>The Halvern Team – Tri-fold Brochure</title>
<link href="https://fonts.googleapis.com/css2?family=Montserrat:wght@400;500;600;700;800&display=swap" rel="stylesheet">
<style>
:root{
  --navy:#1c2472;
  --navy-dark:#141a5a;
  --ink:#3b3f4c;
  --paper:#ffffff;
  --canvas:#ffffff;
  --photo-blue-a:#cfdbe6;
  --photo-blue-b:#8fa6bd;
  --photo-warm-a:#f1ece6;
  --photo-warm-b:#d9c9bc;
  --rule:#c9ccd6;
}
*{margin:0;padding:0;box-sizing:border-box}
html,body{width:800px;height:1200px;overflow:hidden;background:var(--canvas)}
body{font-family:"Montserrat",sans-serif;color:var(--ink);position:relative}
.spread{position:absolute;left:40px;width:720px;height:515px;display:flex;background:var(--paper)}
.spread--outside{top:40px}
.spread--inside{top:610px}
.panel{width:240px;height:100%;display:flex;flex-direction:column;position:relative;overflow:hidden}
.photo{width:100%;flex:none}
.photo--team{background:linear-gradient(135deg,#e9f1f5,#9fc3d3 55%,#d8e4ec)}
.photo--room{background:linear-gradient(160deg,#dfe6ee,#93a9c0 60%,#b9cc9c)}
.photo--doctor-f{background:linear-gradient(180deg,#e6eef4,#b9ccdb 50%,#f2f4f6)}
.photo--doctor-m{background:linear-gradient(180deg,#eef2f5,#c8d3dc 55%,#f3f5f7)}
.photo--clinic{background:linear-gradient(120deg,#e4ecf2,#a9bdcc 50%,#eef1f3)}
.photo--smile{background:linear-gradient(120deg,#fbf5f1,var(--photo-warm-b) 55%,#f0e2dc)}
.body{padding:10px 16px 0}
h2{font-weight:700;font-size:10px;letter-spacing:.4px;color:var(--navy);text-transform:uppercase;margin-bottom:6px}
p{font-size:5.6px;line-height:1.5;text-align:justify;margin-bottom:5px}
p strong,p b{color:var(--navy);font-weight:700}
.section{margin-bottom:8px}
.contact-block{background:var(--navy);color:#fff;text-align:center;padding:12px 0 10px}
.pill{display:inline-block;border-radius:20px;font-weight:700;letter-spacing:.5px}
.pill--light{background:#fff;color:var(--navy);font-size:8.5px;padding:2px 10px}
.contact-block .call{font-size:10px;letter-spacing:1px;margin:8px 0 6px;font-weight:400}
.contact-block .phone{font-size:12px;font-weight:700;letter-spacing:.6px;line-height:1.35}
.addresses{text-align:center;padding-top:10px;font-size:5.2px;color:var(--ink)}
.addresses .item{margin-bottom:7px}
.icon{display:block;margin:0 auto 2px}
.url{background:var(--navy);color:#fff;font-size:8px;font-weight:500;padding:3px 12px;letter-spacing:.3px}
.center{text-align:center}
.brand{display:flex;align-items:center;gap:6px;padding:16px 16px 10px 16px;justify-content:center}
.brand__dot{width:12px;height:12px;border-radius:50%;background:var(--navy);flex:none}
.brand__name{font-size:10px;font-weight:500;color:var(--navy);letter-spacing:.3px}
.cover-title{padding:12px 14px 0;text-align:center}
.cover-title h1{font-weight:800;font-size:20px;color:var(--navy);letter-spacing:.5px;line-height:1}
.cover-title .sub{font-size:10px;color:var(--navy);font-weight:400;letter-spacing:.4px;margin-top:3px}
.cover-title .thanks{font-size:6.4px;margin:8px 20px 8px;text-align:center;line-height:1.45}
.band{background:var(--navy);color:#fff;font-size:6.4px;letter-spacing:.4px;padding:2px 6px;display:inline-block;font-weight:500}
.cover-title .mission{font-size:5.4px;text-align:center;line-height:1.5;margin:6px 22px 10px}
.heading-band{background:var(--navy);color:#fff;padding:10px 16px}
.heading-band h2{color:#fff;margin:0;font-size:9.5px;line-height:1.3}
.welcome-h{font-size:10.5px;line-height:1.25}
</style>
</head>
<body>

<!-- Outside spread -->
<section class="spread spread--outside">
  <article class="panel">
    <div class="photo photo--team" style="height:212px" role="img" aria-label="Photo of a smiling dental assistant and a happy patient giving a thumbs up"></div>
    <div class="body" style="padding-top:14px">
      <div class="section">
        <h2>Patient Care:</h2>
        <p>Needing a root canal is often a surprise and sometimes an emergency. We at The Halvern Team make certain that every patient receives prompt emergency care at any time. We understand how uneasy some patients may feel about dental visits and how we can make a difference in providing a relaxing, positive experience. Our doctors are trained in different levels of sedation dentistry from Nitrous Oxide to Conscious Sedation.</p>
        <p>Our entire team is dedicated to providing you with excellent, personalized care and service to make your visit as comfortable and pleasant as possible. You will enjoy our relaxing treatment rooms, complete with plumacore coverings, televisions and Tunelets for your use during treatment and blankets to keep you warm if you're cold.</p>
      </div>
      <div class="section">
        <h2>Technical Equipment:</h2>
        <p>The Halvern Team prides itself in utilizing the most advanced techniques and state-of-the-art equipment including digital radiography, fiber optic illumination, ultrasonic equipment, and operating microscopes, which help the doctor see microscopic details inside a tooth during micro-surgical and non-surgical procedures.</p>
      </div>
    </div>
  </article>

  <article class="panel">
    <div class="body" style="height:130px;padding-top:14px">
      <h2>Expertise:</h2>
      <p>The Halvern Team is staffed by doctors who are responsive to your concerns and alert to your experience during treatment. All of our doctors are endodontists, which means they are specialists who have completed 2-3 years of advanced training in addition to dental school. We are all specialist members of the Continental Society of Pulp Specialists (CSPS). All our endodontists continue their education and training through professional associations, seminars, study groups, and teaching both at Pellmoor and Dorrin Universities.</p>
    </div>
    <div class="photo photo--room" style="height:148px" role="img" aria-label="Photo of a modern treatment room with a green dental chair"></div>
    <div class="contact-block">
      <span class="pill pill--light">CONTACT US</span>
      <div class="call">CALL US NOW</div>
      <div class="phone">555-014-2290</div>
      <div class="phone">555-014-7731</div>
    </div>
    <div class="addresses">
      <div class="item">
        <svg class="icon" width="9" height="11" viewBox="0 0 10 12"><path d="M5 0C2.2 0 0 2.2 0 4.8 0 8.3 5 12 5 12s5-3.7 5-7.2C10 2.2 7.8 0 5 0z" fill="#1c2472"/><circle cx="5" cy="4.7" r="1.8" fill="#fff"/></svg>
        55 Alder St, Brookvale, MA 01990
      </div>
      <div class="item">
        <svg class="icon" width="9" height="11" viewBox="0 0 10 12"><path d="M5 0C2.2 0 0 2.2 0 4.8 0 8.3 5 12 5 12s5-3.7 5-7.2C10 2.2 7.8 0 5 0z" fill="#1c2472"/><circle cx="5" cy="4.7" r="1.8" fill="#fff"/></svg>
        16 Lantern St, Orchard Falls, MA 01991
      </div>
      <svg class="icon" width="10" height="10" viewBox="0 0 12 12"><circle cx="6" cy="6" r="5.3" fill="none" stroke="#1c2472" stroke-width="1.2"/><ellipse cx="6" cy="6" rx="2.3" ry="5.3" fill="none" stroke="#1c2472" stroke-width="1"/><line x1="0.7" y1="6" x2="11.3" y2="6" stroke="#1c2472" stroke-width="1"/></svg>
      <div style="margin-top:5px"><span class="pill url">www.thehalvernteam.com</span></div>
    </div>
  </article>

  <article class="panel">
    <div class="brand"><span class="brand__dot"></span><span class="brand__name">THE HALVERN TEAM</span></div>
    <div class="photo photo--doctor-f" style="height:232px;margin-left:14px;width:226px" role="img" aria-label="Photo of a smiling female endodontist in a white coat with arms crossed"></div>
    <div class="cover-title">
      <h1>WELCOME TO</h1>
      <div class="sub">THE HALVERN TEAM</div>
      <div class="thanks">Thank you for allowing us to care for your endodontic needs.</div>
      <span class="band">WE LOOK FORWARD TO SERVING YOU</span>
      <div class="mission">We at The Halvern Team have dedicated our professional lives to improving the comfort and dental health of those in our care.</div>
      <span class="pill url">www.thehalvernteam.com</span>
    </div>
  </article>
</section>

<!-- Inside spread -->
<section class="spread spread--inside">
  <article class="panel">
    <div class="body" style="height:250px;padding-top:14px">
      <h2 class="welcome-h">Welcome - On behalf of our staff we welcome you to our office.</h2>
      <p>We are pleased that you have selected our team of professionals to care for your endodontic needs. We want you to know that we are committed to providing you, our patient with the highest quality endodontic care in the most gentle, efficient, and caring manner possible. We pride ourselves on offering our expertise along with the best patient care with the most up to date technologies to better ensure your oral health.</p>
      <p>For your convenience, please visit us online at <b>www.thehalvernteam.com</b> for directions to our offices, pre and post-operative instructions, general information on our Endodontists and much more. We are here for you and our doctors are on <b>call 24 hours a day, 7 days a week.</b></p>
      <p>We are looking forward providing you a most relaxed and pleasant vist possible. Thank you again for choosing The Halvern Team.</p>
    </div>
    <div class="photo photo--doctor-m" style="flex:1" role="img" aria-label="Photo of a smiling male endodontist in a white coat with arms crossed"></div>
  </article>

  <article class="panel">
    <div class="photo photo--clinic" style="height:140px" role="img" aria-label="Photo of dental instruments in a clinic"></div>
    <div class="body" style="height:120px;padding-top:12px">
      <h2>What is a Root Canal?</h2>
      <p>A root canal (endodontic treatment) is one of the most common dental procedures performed, with more than 14 million performed every year. This simple treatment can save your natural teeth and prevent the need of dental implants or bridges.</p>
      <p>At the center of your tooth is pulp. The pulp is a collection of blood vessels, nerves and lymphatics, which help to form the tooth during the stages of tooth development.</p>
    </div>
    <div class="heading-band"><h2>I've already had a root canal, why do I need another procedure?</h2></div>
    <div class="body" style="padding-top:12px">
      <p>Retreatment - A second chance to save your tooth With proper care, most teeth which have had endodontic (root canal) treatment can last as long as other natural teeth.</p>
      <p>However, in a few cases, a tooth that has received endodontic treatment fails to heal completely. And occasionally, a tooth becomes painful or diseased months or even years after previously successful endodontic treatment.</p>
      <p>If your tooth has failed to heal or has developed new problems, you have a second chance. Another endodontic procedure, called retreatment, may be able to save your tooth.</p>
      <p>Retreated teeth can function well for years, even for a lifetime. It's always best to save the tooth if your endodontist believes retreatment is the best option for you.</p>
    </div>
  </article>

  <article class="panel">
    <div class="photo photo--clinic" style="height:140px" role="img" aria-label="Photo of an endodontist and assistant treating a patient"></div>
    <div class="body" style="padding-top:22px">
      <p>Advances in technology are constantly changing the way root canal treatment is performed, so your endodontist may even be able to use a new technique that was not available when you had your first procedure.</p>
      <p>Of course, there are no guarantees with any dental or medical procedure. Your endodontist will discuss your options and the chances of success before beginning retreatment.</p>
      <h2 style="margin-top:10px">What is an Apicoectomy?</h2>
      <p>In this procedure, the endodontist opens the gum tissue near the tooth to see the underlying bone and to remove any inflamed or infected tissue. The very end of the root is also removed or resected.</p>
    </div>
    <div class="photo photo--smile" style="height:180px;margin-top:auto" role="img" aria-label="Close-up photo of a bright smile with a dental mirror"></div>
  </article>
</section>

</body>
</html>
```